Etiketten-Design für Duftsprays
Liebe Kreative
Es geht um ein Premium-Etikettendesign für einen Duftspray. Das Bild der Flasche werde ich Anhängen. Das sichtbare Etikett wird 7.2 x 10.8 cm gross sein. Das Etikett wird jedoch aufklappbar sein, d.h ein Teil wird auf den ersten Blick nicht sichtbar sein.
Die Mindestschriftgrösse ist Arial 7.
Das Design soll schlicht und Premium wirken. Lumidor als Name sollte von oben nach unten geschrieben werden. Dieser Name sollte man hauptsächlich sehen, wenn man es von vorne betrachtet. Wichtig ist noch, dass beim sichtbaren Teil steht „Innenseite beachten“
Sichtbarer Teil:
Lumidor (Produktname)
Inhalt: 30 ml
Gefahrenpiktogramme (Im Anhang. Auf Etikette 1x1cm gross)
Pelsa GMBH
CH-8517 Talbrunn
Tel. 022 384 57 90
Enthält / Contient: 2-Propanol
Lumidor zweimal auf Kopfhöhe und 30cm vor dem Gesicht in die Luft sprühen und einatmen. Fördert die Konzentration und macht wach.
Innenseite beachten.
Nicht sichtbarer Teil:
ACHTUNG Kann Schläfrigkeit und Benommenheit verursachen Enthält D-Limonen, Citral. Kann allergische Reaktionen hervorrufen. Darf nicht in die Hände von Kindern gelangen.
ATTENTION Peut provoquer somnolence ou vertiges. Contient d-limonène, citral. Peut produire une réaction allergique. Tenir hors de portée des enfants.
Haltbarkeit: Nach dem Öffnen 6 Monate haltbar
Aufgabenstellung
Es ist wichtig, dass das ganze Stilvoll aussieht, es soll eine 'Premium-Ausstrahlung' haben.

```html
<!DOCTYPE html>
<html lang="de">
<head>
<meta charset="utf-8">
<title>Lumidor – Etikettendesign</title>
<link href="https://fonts.googleapis.com/css2?family=Marcellus&family=Alegreya+Sans:wght@400;700&display=swap" rel="stylesheet">
<style>
  :root {
    --ink: #6f6f6f;
    --ink-soft: #8c8c8c;
    --rule: #9a9a9a;
    --paper: #ffffff;
    --stage-edge: #efefef;
    --gold-light: #f5e39a;
    --gold-dark: #b88a2a;
    --glass: #ececec;
    --brand: "Marcellus", serif;
    --body: "Alegreya Sans", sans-serif;
  }
  * { margin: 0; padding: 0; box-sizing: border-box; }
  html, body { width: 857px; height: 1200px; overflow: hidden; background: var(--paper); }
  .sheet { position: relative; width: 857px; height: 1200px; color: var(--ink); font-family: var(--body); font-variant-numeric: lining-nums; }
  b { font-weight: 700; }

  /* Produktbühne */
  .stage { position: absolute; left: 0; top: 0; width: 857px; height: 557px;
    background: linear-gradient(180deg, var(--stage-edge) 0%, var(--paper) 9%, var(--paper) 86%, var(--stage-edge) 100%); }
  .bottle { position: absolute; top: 99px; width: 48px; height: 359px; }
  .bottle-cap { position: absolute; left: 3px; top: 0; width: 42px; height: 44px; border-radius: 3px 3px 0 0;
    background: linear-gradient(90deg, var(--gold-dark), var(--gold-light) 45%, var(--gold-dark)); }
  .bottle-collar { position: absolute; left: 0; top: 42px; width: 48px; height: 33px; border-radius: 2px;
    background: linear-gradient(90deg, var(--gold-dark), var(--gold-light) 45%, var(--gold-dark)); }
  .bottle-neck { position: absolute; left: 2px; top: 75px; width: 44px; height: 25px;
    background: linear-gradient(90deg, #dcdcdc, #f7f7f7 50%, #dcdcdc); }
  .bottle-label { position: absolute; left: 0; top: 100px; width: 48px; height: 251px;
    background: linear-gradient(90deg, #ececec, #fff 12%, #fff 88%, #ececec); }
  .bottle-base { position: absolute; left: 2px; top: 351px; width: 44px; height: 8px; border-radius: 0 0 6px 6px;
    background: linear-gradient(90deg, #d8d8d8, #f4f4f4 50%, #d8d8d8); }
  .bottle-1 { left: 204px; } .bottle-2 { left: 309px; } .bottle-3 { left: 585px; }

  /* Gedrehtes Etikett – gemeinsames Raster (308 × 308) */
  .turned { position: absolute; width: 308px; height: 308px; }
  .scaled { transform: scale(0.789); transform-origin: 0 0; }
  .up { writing-mode: vertical-rl; transform: rotate(180deg); white-space: nowrap; }
  .down { writing-mode: vertical-rl; white-space: nowrap; }
  .t-warnings { position: absolute; left: 12px; top: 14px; height: 282px; font-size: 8px; line-height: 1.05; }
  .t-warnings p + p { margin-left: 7px; }
  .t-warnings b { letter-spacing: 0.04em; }
  .t-fold { position: absolute; left: 103px; top: 2px; bottom: 2px; border-left: 0.8px dashed var(--rule); }
  .t-info { position: absolute; left: 110px; top: 11px; height: 285px; font-size: 8px; line-height: 1.1; text-align: center; }
  .t-info p + p { margin-left: 5px; }
  .t-hazards { position: absolute; left: 63px; top: 11px; }
  .t-brand { position: absolute; left: 218px; top: 0; height: 308px; font-family: var(--brand); font-size: 24px; line-height: 26px;
    letter-spacing: 0.35em; padding-inline-start: 0.35em; text-align: center; }
  .t-note { position: absolute; left: 295px; top: 0; height: 308px; font-size: 6.6px; line-height: 8px; letter-spacing: 0.28em;
    padding-inline-start: 0.28em; text-align: center; color: var(--ink-soft); }
  .t-volume { position: absolute; left: 212px; top: 286px; font-size: 9px; line-height: 10px; white-space: nowrap; }
  .corner-tr { position: absolute; right: 3px; top: 3px; width: 0; height: 0; border-top: 7px solid var(--ink); border-left: 7px solid transparent; }
  .corner-br { position: absolute; right: 3px; bottom: 3px; width: 0; height: 0; border-bottom: 7px solid var(--ink); border-left: 7px solid transparent; }
  .framed { border: 0.8px solid var(--rule); }

  /* Spezifikation */
  .spec { position: absolute; left: 29px; top: 586px; font-size: 10px; line-height: 14px; letter-spacing: 0.14em; color: var(--ink-soft); }
  .wordmark { position: absolute; left: 0; width: 857px; top: 658px; text-align: center; font-family: var(--brand); font-weight: 400;
    font-size: 29px; line-height: 34px; letter-spacing: 0.35em; padding-left: 0.35em; }
  .tagline { position: absolute; left: 0; width: 857px; top: 700px; text-align: center; font-family: var(--brand);
    font-size: 12px; line-height: 14px; letter-spacing: 0.5em; padding-left: 0.5em; }

  /* Flaches Etikett */
  .label { position: absolute; top: 786px; width: 308px; height: 308px; background: var(--paper); }
  .label-flat { left: 86px; }
  .label-turned { left: 462px; }
  .f-warnings { position: absolute; left: 10px; top: 10px; width: 290px; font-size: 8.4px; line-height: 1.1; }
  .f-warnings p + p { margin-top: 8px; }
  .f-warnings b { letter-spacing: 0.04em; }
  .f-hazards { position: absolute; left: 234px; top: 61px; }
  .f-fold { position: absolute; left: 2px; right: 2px; top: 101px; border-top: 0.8px dashed var(--rule); }
  .f-info { position: absolute; left: 0; right: 0; top: 110px; font-size: 8.4px; line-height: 1.1; text-align: center; }
  .f-info p + p { margin-top: 5px; }
  .f-brand { position: absolute; left: 0; right: 0; top: 213px; text-align: center; font-family: var(--brand);
    font-size: 22px; line-height: 26px; letter-spacing: 0.36em; padding-left: 0.36em; }
  .f-volume { position: absolute; left: 10px; top: 208px; font-size: 8.4px; line-height: 10px; }
  .f-note { position: absolute; left: 0; right: 0; top: 289px; text-align: center; font-size: 6.6px; line-height: 8px;
    letter-spacing: 0.28em; padding-left: 0.28em; color: var(--ink-soft); }
</style>
</head>
<body>
<main class="sheet">

  <section class="stage">
    <div class="bottle bottle-1" role="img" aria-label="Sprayflasche mit Goldkappe">
      <div class="bottle-cap"></div><div class="bottle-collar"></div><div class="bottle-neck"></div>
      <div class="bottle-label"></div><div class="bottle-base"></div>
    </div>
    <div class="bottle bottle-2" role="img" aria-label="Sprayflasche mit Goldkappe, Rückseite">
      <div class="bottle-cap"></div><div class="bottle-collar"></div><div class="bottle-neck"></div>
      <div class="bottle-label"></div><div class="bottle-base"></div>
    </div>
    <div class="bottle bottle-3" role="img" aria-label="Sprayflasche mit Goldkappe und aufgeklapptem Etikett">
      <div class="bottle-cap"></div><div class="bottle-collar"></div><div class="bottle-neck"></div>
      <div class="bottle-label"></div><div class="bottle-base"></div>
    </div>

    <!-- Vorderseite auf Flasche 1 -->
    <div class="turned scaled" style="left:47px; top:197px;">
      <span class="t-brand up">LUMIDOR</span>
      <span class="t-volume">℮ 30 ml</span>
    </div>

    <!-- Rückseite auf Flasche 2 -->
    <div class="turned scaled" style="left:228px; top:197px;">
      <div class="t-info up">
        <p>Pelsa GMBH · CH-8517 Talbrunn · Tel. 022 384 57 90</p>
        <p><b>Enthält / Contient:</b> 2-Propanol</p>
        <p>Lumidor zweimal auf Kopfhöhe und 30 cm vor dem Gesicht in die<br>Luft sprühen und einatmen. Fördert die Konzentration und macht wach.</p>
      </div>
    </div>

    <!-- Aufgeklapptes Etikett an Flasche 3 -->
    <div class="turned scaled framed" style="left:429px; top:197px;">
      <div class="t-warnings up">
        <p><b>ACHTUNG:</b> Kann Schläfrigkeit und Benommenheit verursachen.<br>Enthält D-Limonen, Citral. Kann allergische Reaktionen hervorrufen.<br>Darf nicht in die Hände von Kindern gelangen.</p>
        <p><b>ATTENTION:</b> Peut provoquer somnolence ou vertiges.<br>Contient d-limonène, citral. Peut produire une réaction<br>allergique. Tenir hors de portée des enfants.</p>
        <p><b>Haltbarkeit:</b> Nach dem Öffnen 6 Monate haltbar.</p>
      </div>
      <svg class="t-hazards" width="30" height="64" viewBox="0 0 30 64" aria-label="Gefahrenpiktogramme">
        <g fill="none" stroke="#6f6f6f" stroke-width="1.6">
          <path d="M15 1 L29 15 L15 29 L1 15 Z"/>
          <path d="M15 35 L29 49 L15 63 L1 49 Z"/>
        </g>
        <path d="M13.8 8h2.4l-.4 8.5h-1.6z M15 18.5a1.3 1.3 0 1 1 0 2.6a1.3 1.3 0 0 1 0-2.6z" fill="#6f6f6f"/>
        <path d="M15 41c3.5 2.8 4.2 5.8 2.2 8.6c-1.4 1.8-5.4 1.4-5.6-1.4c-.1-2 1.4-2.8 1.7-4.5c.8 1.1.8 2 .6 2.8c2-1.1 1.8-3.4 1.1-5.5z M9.5 53h11" fill="#6f6f6f" stroke="#6f6f6f" stroke-width=".8"/>
      </svg>
      <div class="t-fold"></div>
      <div class="t-info up">
        <p>Pelsa GMBH · CH-8517 Talbrunn · Tel. 022 384 57 90</p>
        <p><b>Enthält / Contient:</b> 2-Propanol</p>
        <p>Lumidor zweimal auf Kopfhöhe und 30 cm vor dem Gesicht in die<br>Luft sprühen und einatmen. Fördert die Konzentration und macht wach.</p>
      </div>
      <span class="t-brand up">LUMIDOR</span>
      <span class="t-note up">INNENSEITE BEACHTEN</span>
      <span class="t-volume">℮ 30 ml</span>
      <span class="corner-tr"></span>
    </div>
  </section>

  <p class="spec">ETIKETT 72 X 108 MM (108 X 108 MM)</p>
  <h1 class="wordmark">LUMIDOR</h1>
  <p class="tagline">YOUR TAGLINE</p>

  <article class="label label-flat framed">
    <div class="f-warnings">
      <p><b>ACHTUNG:</b> Kann Schläfrigkeit und Benommenheit verursachen.<br>Enthält D-Limonen, Citral. Kann allergische Reaktionen hervorrufen.<br>Darf nicht in die Hände von Kindern gelangen.</p>
      <p><b>ATTENTION:</b> Peut provoquer somnolence ou vertiges.<br>Contient d-limonène, citral. Peut produire une réaction<br>allergique. Tenir hors de portée des enfants.</p>
      <p><b>Haltbarkeit:</b> Nach dem Öffnen 6 Monate haltbar.</p>
    </div>
    <svg class="f-hazards" width="64" height="30" viewBox="0 0 64 30" aria-label="Gefahrenpiktogramme">
      <g fill="none" stroke="#6f6f6f" stroke-width="1.6">
        <path d="M15 1 L29 15 L15 29 L1 15 Z"/>
        <path d="M49 1 L63 15 L49 29 L35 15 Z"/>
      </g>
      <path d="M15 7c3.5 2.8 4.2 5.8 2.2 8.6c-1.4 1.8-5.4 1.4-5.6-1.4c-.1-2 1.4-2.8 1.7-4.5c.8 1.1.8 2 .6 2.8c2-1.1 1.8-3.4 1.1-5.5z M9.5 19h11" fill="#6f6f6f" stroke="#6f6f6f" stroke-width=".8"/>
      <path d="M47.8 8h2.4l-.4 8.5h-1.6z M49 18.5a1.3 1.3 0 1 1 0 2.6a1.3 1.3 0 0 1 0-2.6z" fill="#6f6f6f"/>
    </svg>
    <div class="f-fold"></div>
    <div class="f-info">
      <p>Pelsa GMBH · CH-8517 Talbrunn · Tel. 022 384 57 90</p>
      <p><b>Enthält / Contient:</b> 2-Propanol</p>
      <p>Lumidor zweimal auf Kopfhöhe und 30 cm vor dem Gesicht in die<br>Luft sprühen und einatmen. Fördert die Konzentration und macht wach.</p>
    </div>
    <span class="f-volume down">℮ 30 ml</span>
    <span class="f-brand">LUMIDOR</span>
    <span class="f-note">INNENSEITE BEACHTEN</span>
    <span class="corner-br"></span>
  </article>

  <article class="label label-turned framed">
    <div class="t-warnings up">
      <p><b>ACHTUNG:</b> Kann Schläfrigkeit und Benommenheit verursachen.<br>Enthält D-Limonen, Citral. Kann allergische Reaktionen hervorrufen.<br>Darf nicht in die Hände von Kindern gelangen.</p>
      <p><b>ATTENTION:</b> Peut provoquer somnolence ou vertiges.<br>Contient d-limonène, citral. Peut produire une réaction<br>allergique. Tenir hors de portée des enfants.</p>
      <p><b>Haltbarkeit:</b> Nach dem Öffnen 6 Monate haltbar.</p>
    </div>
    <svg class="t-hazards" width="30" height="64" viewBox="0 0 30 64" aria-label="Gefahrenpiktogramme">
      <g fill="none" stroke="#6f6f6f" stroke-width="1.6">
        <path d="M15 1 L29 15 L15 29 L1 15 Z"/>
        <path d="M15 35 L29 49 L15 63 L1 49 Z"/>
      </g>
      <path d="M13.8 8h2.4l-.4 8.5h-1.6z M15 18.5a1.3 1.3 0 1 1 0 2.6a1.3 1.3 0 0 1 0-2.6z" fill="#6f6f6f"/>
      <path d="M15 41c3.5 2.8 4.2 5.8 2.2 8.6c-1.4 1.8-5.4 1.4-5.6-1.4c-.1-2 1.4-2.8 1.7-4.5c.8 1.1.8 2 .6 2.8c2-1.1 1.8-3.4 1.1-5.5z M9.5 53h11" fill="#6f6f6f" stroke="#6f6f6f" stroke-width=".8"/>
    </svg>
    <div class="t-fold"></div>
    <div class="t-info up">
      <p>Pelsa GMBH · CH-8517 Talbrunn · Tel. 022 384 57 90</p>
      <p><b>Enthält / Contient:</b> 2-Propanol</p>
      <p>Lumidor zweimal auf Kopfhöhe und 30 cm vor dem Gesicht in die<br>Luft sprühen und einatmen. Fördert die Konzentration und macht wach.</p>
    </div>
    <span class="t-brand up">LUMIDOR</span>
    <span class="t-note up">INNENSEITE BEACHTEN</span>
    <span class="t-volume">℮ 30 ml</span>
    <span class="corner-tr"></span>
  </article>

</main>
</body>
</html>
```